Residential & commercial cleaning business

Looking for Brazilian colors, green/blue/yellow.
Name of business is “Marla’s Cleaning”.
Second side of card will be for ‘confirming customer next appointment date/time.
Want to include in description…residential & commercial cleaning, experienced, highly recommended, reasonable rates, free estimates, Marla’sCleaningVT@brightmop.com, Maplewood Falls, VT, Call today at 802.517.3946.

```html
<!DOCTYPE html>
<html lang="en">
<head>
<meta charset="utf-8">
<title>Marla’s Cleaning – Business Card</title>
<link href="https://fonts.googleapis.com/css2?family=Montserrat:wght@400;500;600;700&display=swap" rel="stylesheet">
<style>
  :root {
    --backdrop: #4f4f4f;
    --card-white: #ffffff;
    --brand-green: #6a9a2e;
    --brand-yellow: #f9e000;
    --brand-blue: #16a3d6;
    --text-white: #ffffff;
  }
  * { box-sizing: border-box; margin: 0; padding: 0; }
  html, body {
    width: 1200px;
    height: 1200px;
    overflow: hidden;
    background: var(--backdrop);
    font-family: "Montserrat", Arial, sans-serif;
  }
  .card {
    position: absolute;
    left: 186px;
    width: 828px;
    height: 460px;
    overflow: hidden;
  }
  /* Front */
  .card-front { top: 113px; background: var(--card-white); }
  .brand-name {
    position: absolute;
    left: 40px;
    top: 140px;
    width: 380px;
    text-align: center;
    color: var(--brand-green);
    font-weight: 600;
    font-size: 40px;
    line-height: 1.1;
  }
  .services {
    position: absolute;
    left: 499px;
    top: 92px;
    color: var(--brand-green);
    font-weight: 500;
    font-size: 37px;
    line-height: 38px;
  }
  .call-label {
    position: absolute;
    left: 502px;
    top: 218px;
    color: var(--brand-green);
    font-weight: 700;
    font-size: 21px;
  }
  .phone-pill {
    position: absolute;
    left: 474px;
    top: 258px;
    width: 306px;
    height: 80px;
    border-radius: 40px;
    background: var(--brand-yellow);
    color: var(--brand-green);
    font-weight: 700;
    font-size: 35px;
    line-height: 80px;
    padding-left: 42px;
    letter-spacing: 0.5px;
  }
  .feature-band {
    position: absolute;
    left: 0;
    bottom: 0;
    width: 100%;
    height: 87px;
    background: var(--brand-blue);
    color: var(--text-white);
    font-weight: 700;
    font-size: 19.4px;
    line-height: 87px;
    text-align: center;
  }
  /* Back */
  .card-back { top: 628px; background: var(--brand-blue); }
  .appointment-title {
    position: absolute;
    left: 0;
    top: 70px;
    width: 100%;
    text-align: center;
    color: var(--text-white);
    font-weight: 500;
    font-size: 57px;
    line-height: 66px;
  }
  .field {
    position: absolute;
    height: 64px;
    border-radius: 32px;
    background: var(--card-white);
    border: 3px solid var(--brand-green);
    color: var(--brand-green);
    font-weight: 500;
    font-size: 24px;
    line-height: 58px;
    padding-left: 24px;
  }
  .field-date { left: 67px; top: 182px; width: 324px; }
  .field-time { left: 431px; top: 182px; width: 324px; }
  .field-details { left: 67px; top: 268px; width: 688px; border-color: var(--card-white); }
  .contact {
    position: absolute;
    left: 0;
    top: 343px;
    width: 100%;
    text-align: center;
    color: var(--text-white);
    font-size: 24px;
    line-height: 33px;
    font-weight: 500;
  }
</style>
</head>
<body>
  <section class="card card-front">
    <div class="brand-name">Marla’s Cleaning</div>
    <h2 class="services">Residential<br>&amp; Commercial<br>cleaning</h2>
    <p class="call-label">Call today at</p>
    <div class="phone-pill">802.517.3946</div>
    <div class="feature-band">Experienced, Highly recommended, Reasonable Rates, Free estimates</div>
  </section>

  <section class="card card-back">
    <h1 class="appointment-title">Your next appointment</h1>
    <div class="field field-date">Date:</div>
    <div class="field field-time">Time:</div>
    <div class="field field-details">Details:</div>
    <div class="contact">
      <p>Maplewood Falls, VT</p>
      <p>Marla’sCleaningVT@brightmop.com</p>
    </div>
  </section>
</body>
</html>
```